Harborline Self Storage

looking for a clean sharp easy to read advertising billboard to rent units

online rentals
online payment
online check out

climate control units available
competitive rates

https://www.harborline-selfstorage.example/

```html
<!DOCTYPE html>
<html lang="en">
<head>
<meta charset="utf-8">
<title>Harborline Self Storage — Billboard</title>
<link rel="stylesheet" href="https://fonts.googleapis.com/css2?family=Anton&family=Montserrat:wght@600;700&family=Oswald:wght@500&display=swap">
<style>
  :root {
    --navy: #262a5e;
    --red: #e30613;
    --white: #ffffff;
    --backdrop: #e9ebef;
  }
  * { margin: 0; padding: 0; box-sizing: border-box; }
  html, body {
    width: 1200px;
    height: 1157px;
    overflow: hidden;
    background: var(--backdrop);
  }
  .billboard {
    position: absolute;
    left: 0;
    top: 307px;
    width: 1200px;
    height: 542px;
    background: var(--white);
    overflow: hidden;
  }
  .brand-band {
    position: absolute;
    left: 0; top: 0;
    width: 1200px; height: 247px;
    display: flex;
    align-items: center;
    justify-content: center;
    gap: 26px;
  }
  .brand-dot {
    width: 54px; height: 54px;
    border-radius: 50%;
    background: var(--red);
  }
  .brand-name {
    font-family: "Anton", sans-serif;
    font-size: 86px;
    color: var(--navy);
    letter-spacing: 1px;
    line-height: 1;
  }
  .info-band {
    position: absolute;
    left: 0; top: 247px;
    width: 1200px; height: 206px;
    background: var(--navy);
  }
  .features {
    position: absolute;
    left: 92px; top: 46px;
    list-style: none;
  }
  .features li {
    display: flex;
    align-items: center;
    height: 46px;
    font-family: "Montserrat", sans-serif;
    font-weight: 700;
    font-size: 33px;
    letter-spacing: 2.5px;
    color: var(--white);
  }
  .features svg { width: 30px; height: 30px; margin-right: 17px; flex: none; }
  .highlights {
    position: absolute;
    left: 753px; top: 24px;
    width: 335px;
    text-align: center;
    font-family: "Anton", sans-serif;
    color: var(--white);
    font-size: 43px;
    line-height: 1;
  }
  .highlights p { height: 56px; display: flex; align-items: center; justify-content: center; }
  .highlights .tag {
    background: var(--red);
    border-radius: 8px;
    height: 58px;
  }
  .contact-band {
    position: absolute;
    left: 0; top: 453px;
    width: 1200px; height: 89px;
  }
  .contact-band svg { position: absolute; left: 0; top: 0; }
  .website {
    position: absolute;
    left: 80px; top: 20px;
    font-family: "Montserrat", sans-serif;
    font-weight: 600;
    font-size: 31px;
    color: var(--white);
    letter-spacing: 0.5px;
  }
  .phone {
    position: absolute;
    left: 700px; top: 4px;
    font-family: "Oswald", sans-serif;
    font-weight: 500;
    font-size: 72px;
    line-height: 1.1;
    letter-spacing: 3px;
    color: var(--navy);
  }
</style>
</head>
<body>
  <main class="billboard">
    <header class="brand-band">
      <span class="brand-dot"></span>
      <h1 class="brand-name">HARBORLINE SELF STORAGE</h1>
    </header>

    <section class="info-band">
      <ul class="features">
        <li><svg viewBox="0 0 30 30"><circle cx="15" cy="15" r="15" fill="var(--red)"/><path d="M12 8l7 7-7 7" fill="none" stroke="var(--navy)" stroke-width="3.5" stroke-linecap="round" stroke-linejoin="round"/></svg>ONLINE RENTALS</li>
        <li><svg viewBox="0 0 30 30"><circle cx="15" cy="15" r="15" fill="var(--red)"/><path d="M12 8l7 7-7 7" fill="none" stroke="var(--navy)" stroke-width="3.5" stroke-linecap="round" stroke-linejoin="round"/></svg>ONLINE PAYMENT</li>
        <li><svg viewBox="0 0 30 30"><circle cx="15" cy="15" r="15" fill="var(--red)"/><path d="M12 8l7 7-7 7" fill="none" stroke="var(--navy)" stroke-width="3.5" stroke-linecap="round" stroke-linejoin="round"/></svg>ONLINE CHECK OUT</li>
      </ul>
      <div class="highlights">
        <p>CLIMATE CONTROL</p>
        <p class="tag">UNITS AVAILABLE</p>
        <p>COMPETITIVE RATES</p>
      </div>
    </section>

    <footer class="contact-band">
      <svg width="1200" height="89" viewBox="0 0 1200 89">
        <rect x="0" y="0" width="1200" height="7" fill="var(--red)"/>
        <polygon points="73,0 652,0 588,89 0,89" fill="var(--red)"/>
      </svg>
      <span class="website">harborline-selfstorage.example</span>
      <span class="phone">412-555-0190</span>
    </footer>
  </main>
</body>
</html>
```